Ridgeway Pest Solutions *

I work as a pest control technician with other company. Now I want to start my own business.

So I want a new logo and business card design (both side of the card).

Colour combination I like Green/Red/white.

On card may have some sort of insect/ but not sure.

Target Market(s)

Anyone in Sydney. There is no specific target.

Industry/Entity Type

Business

Logo Text

Ridgeway Pest Solutions

```html
<!DOCTYPE html>
<html lang="en">
<head>
<meta charset="utf-8">
<title>Ridgeway Pest Solutions – Business Card</title>
<link href="https://fonts.googleapis.com/css2?family=Roboto:wght@400;500;700&display=swap" rel="stylesheet">
<style>
  :root {
    --page-bg: #e6e4e1;
    --card-white: #ffffff;
    --card-mist: #f1f0ef;
    --charcoal: #3b3939;
    --brand-red: #d3121c;
    --ink: #1e1e1e;
    --on-dark: #ffffff;
  }
  * { margin: 0; padding: 0; box-sizing: border-box; }
  html, body {
    width: 1200px; height: 900px; overflow: hidden;
    background: var(--page-bg);
    font-family: "Roboto", Arial, sans-serif;
  }
  .business-card {
    position: absolute; left: 120px; top: 153px;
    width: 960px; height: 594px;
    background: linear-gradient(100deg, var(--card-white) 40%, var(--card-mist) 100%);
    box-shadow: 0 10px 30px rgba(0,0,0,.15);
    overflow: hidden;
  }
  .dark-panel { position: absolute; inset: 0; width: 960px; height: 594px; }
  .holder {
    position: absolute; right: 57px; top: 84px; text-align: right;
  }
  .holder-name {
    color: var(--brand-red); font-weight: 700; font-size: 32px; letter-spacing: .5px;
    line-height: 1.1;
  }
  .holder-role { color: var(--ink); font-size: 25px; line-height: 1.3; margin-top: 2px; margin-right: 4px; }
  .address {
    position: absolute; right: 57px; top: 178px; text-align: right;
    color: var(--ink); font-size: 25px; line-height: 34px;
  }
  .contacts {
    position: absolute; left: 52px; top: 404px; list-style: none;
    color: var(--on-dark); font-size: 26px; line-height: 35px;
  }
  .contacts li { display: flex; align-items: center; gap: 8px; }
  .contacts svg { width: 18px; height: 18px; flex: none; }
  .brand {
    position: absolute; left: 518px; top: 423px;
    display: flex; align-items: center; gap: 18px;
  }
  .brand-dot {
    width: 110px; height: 110px; border-radius: 50%;
    border: 5px solid var(--brand-red);
  }
  .brand-name {
    color: var(--brand-red); font-weight: 700; font-size: 30px;
    line-height: 34px; letter-spacing: 1px; text-transform: uppercase;
  }
</style>
</head>
<body>
  <main class="business-card">
    <svg class="dark-panel" viewBox="0 0 960 594" preserveAspectRatio="none" aria-hidden="true">
      <path d="M0,0 H500 C380,120 340,260 450,340 C520,400 430,500 415,594 H0 Z" fill="var(--charcoal)"/>
      <path d="M500,0 C380,120 340,260 450,340 C520,400 430,500 415,594" fill="none" stroke="var(--brand-red)" stroke-width="3"/>
    </svg>

    <div class="holder">
      <p class="holder-name">DANIEL HARPER</p>
      <p class="holder-role">Managing Director</p>
    </div>
    <p class="address">12 Harbour Street<br>Sydney NSW,2000</p>

    <ul class="contacts">
      <li>
        <svg viewBox="0 0 20 20"><path fill="var(--brand-red)" d="M3 5c0-1 1-2 2-2h10c1 0 2 1 2 2v2h-4V5H7v2H3z M5 9h10l2 7H3z"/></svg>
        444 555 7291
      </li>
      <li>
        <svg viewBox="0 0 20 20"><rect x="2" y="4" width="16" height="12" fill="var(--brand-red)"/><path d="M2 4l8 7 8-7" fill="none" stroke="var(--charcoal)" stroke-width="1.5"/></svg>
        info@ridgewaypest.com
      </li>
      <li>
        <svg viewBox="0 0 20 20"><circle cx="10" cy="10" r="8" fill="var(--brand-red)"/><path d="M2 10h16M10 2c-4 4-4 12 0 16M10 2c4 4 4 12 0 16" fill="none" stroke="var(--charcoal)" stroke-width="1"/></svg>
        www.ridgewaypest.com
      </li>
    </ul>

    <div class="brand">
      <span class="brand-dot" aria-hidden="true"></span>
      <p class="brand-name">Ridgeway Pest<br>Solutions</p>
    </div>
  </main>
</body>
</html>
```